How it Works Diagram for Marketing Agency

We'd like a new "How it Works" diagram for our marketing agency's lead generation service offering. We'd like a traditional sales funnel-like diagram that conveys more prospects towards the top of the funnel and fewer towards the bottom. My website is VelmarkPartners.com so you can see the color scheme there as well.

See a current presentation we have here: https://slides.quornaview.net/deck/7kq_RbnWZ38pLtuyxMENgh_fZcaoLdVRJPOWKEPzbNRs/edit#page=id.h4cbfe2071_0_0

Explanation of image I drew on the whiteboard:

Top says: B2B Lookalike Audiences or ABM Lists

Data 1-4 can be replaced with the data companies used on slide 5 with the 5 data company logos there.

The next section is showing that there are fewer prospects. The tactics we do in this section are: Outreach & Offer, Pre-Qualification Question, Email Follow up

The 3rd section is Appointment Setting.

Target Market(s)

B2B enterprise level businesses

Industry/Entity Type

Digital Marketing

Font styles to use
Serif
Sans Serif

Colors
faa54b
f37122

Requirements
Must have
• Must use a similar color scheme or a matching color scheme to my brand colors so it will look good both on the web pages as well as on presentation docs.

```html
<!DOCTYPE html>
<html lang="en">
<head>
<meta charset="utf-8">
<title>How It Works – Velmark Partners</title>
<link href="https://fonts.googleapis.com/css2?family=Montserrat:wght@500;800&family=Roboto+Condensed:wght@400;700&display=swap" rel="stylesheet">
<style>
  :root {
    --orange: #f37122;
    --amber: #faa54b;
    --gold: #f7c23a;
    --navy: #24345a;
    --blue: #2f5e9e;
    --sky: #5fa0dc;
    --ink: #3c3f46;
    --slate: #6f8aa3;
    --rule: #e7e7ea;
    --paper: #ffffff;
  }
  * { box-sizing: border-box; margin: 0; padding: 0; }
  html, body { width: 1200px; height: 849px; overflow: hidden; background: var(--paper); }
  body { position: relative; font-family: "Roboto Condensed", "Arial Narrow", sans-serif; color: var(--navy); }
  .diagram-art { position: absolute; inset: 0; width: 1200px; height: 849px; }
  .t { position: absolute; white-space: nowrap; }
  .brand { left: 0; width: 1294px; top: 74px; text-align: center; }
  .brand-row { display: inline-flex; align-items: center; gap: 8px; }
  .brand-dot { width: 42px; height: 42px; border-radius: 50%; background: var(--orange); }
  .brand-text { text-align: left; }
  .brand-name { display: block; font-family: "Montserrat", sans-serif; font-weight: 800; font-size: 20px; color: var(--ink); line-height: 1; }
  .brand-tag { display: block; font-family: "Montserrat", sans-serif; font-weight: 500; font-size: 8.5px; letter-spacing: 3px; color: var(--ink); margin-top: 4px; }
  .stage-title { left: 248px; width: 300px; text-align: center; font-weight: 700; font-size: 16px; }
  .stage-title .accent { color: var(--orange); }
  .title-1 { top: 233px; }
  .title-2 { top: 262px; color: var(--orange); }
  .partner { font-family: "Roboto Condensed", sans-serif; font-weight: 700; font-size: 27px; line-height: 1; }
  .p-orvanta { left: 641px; top: 338px; color: var(--slate); }
  .p-pellucid { left: 784px; top: 338px; color: var(--orange); }
  .p-keystat { left: 606px; top: 406px; color: var(--blue); font-size: 22px; }
  .p-tidewell { left: 776px; top: 406px; color: var(--slate); font-size: 22px; }
  .p-marrowline { left: 920px; top: 406px; color: #111; font-size: 22px; }
  .step-label { font-weight: 700; font-size: 13px; text-align: center; width: 240px; }
  .s-outreach { left: 478px; top: 561px; }
  .s-prequal { left: 732px; top: 558px; }
  .s-email { left: 971px; top: 558px; }
  .s-appoint { left: 449px; top: 681px; }
</style>
</head>
<body>
<svg class="diagram-art" viewBox="0 0 1200 849" xmlns="http://www.w3.org/2000/svg">
  <defs>
    <linearGradient id="warm" x1="0" y1="0" x2="1" y2="0">
      <stop offset="0" stop-color="var(--orange)"/>
      <stop offset="0.55" stop-color="var(--amber)"/>
      <stop offset="1" stop-color="var(--gold)"/>
    </linearGradient>
    <linearGradient id="cool" x1="0" y1="0" x2="1" y2="0">
      <stop offset="0" stop-color="var(--navy)"/>
      <stop offset="0.5" stop-color="var(--blue)"/>
      <stop offset="1" stop-color="var(--sky)"/>
    </linearGradient>
  </defs>

  <!-- audience search icon -->
  <g fill="none" stroke="var(--navy)" stroke-width="2.4">
    <circle cx="394" cy="194" r="13"/>
    <line x1="403" y1="204" x2="413" y2="214" stroke="var(--orange)" stroke-width="4" stroke-linecap="round"/>
  </g>

  <!-- funnel stages -->
  <path class="funnel-top" d="M183 313 L612 313 L546 462 L249 462 Z" fill="url(#warm)" opacity="0.85" role="img" aria-label="Dotted funnel band: wide pool of prospects"/>
  <path class="funnel-mid" d="M264 480 L531 480 L474 609 L321 609 Z" fill="url(#cool)" opacity="0.85" role="img" aria-label="Dotted funnel band: fewer engaged prospects"/>
  <path class="funnel-bottom" d="M336 625 L460 625 L414 694 L364 694 Z" fill="var(--navy)" opacity="0.9" role="img" aria-label="Dotted funnel band: booked appointments"/>

  <!-- divider and rules -->
  <line x1="636" y1="319" x2="450" y2="693" stroke="var(--orange)" stroke-width="1.6"/>
  <line x1="574" y1="460" x2="1144" y2="460" stroke="var(--rule)" stroke-width="4"/>
  <line x1="489" y1="604" x2="1187" y2="604" stroke="var(--rule)" stroke-width="4"/>

  <!-- outreach icon: speech bubble -->
  <path d="M580 508 h34 a5 5 0 0 1 5 5 v16 a5 5 0 0 1 -5 5 h-20 l-8 7 v-7 h-6 a5 5 0 0 1 -5 -5 v-16 a5 5 0 0 1 5 -5 z" fill="none" stroke="var(--navy)" stroke-width="1.8"/>
  <g fill="var(--orange)">
    <circle cx="588" cy="521" r="2.2"/><circle cx="597" cy="521" r="2.2"/><circle cx="606" cy="521" r="2.2"/>
  </g>

  <!-- arrows -->
  <g stroke="#8c8c8c" stroke-width="1.2" stroke-dasharray="2 2">
    <line x1="674" y1="523" x2="718" y2="523"/>
    <line x1="955" y1="523" x2="997" y2="523"/>
  </g>
  <path d="M718 520 L724 523 L718 526 Z" fill="#8c8c8c"/>
  <path d="M997 520 L1003 523 L997 526 Z" fill="#8c8c8c"/>

  <!-- pre-qualification icon -->
  <g fill="none" stroke="var(--navy)" stroke-width="1.6">
    <rect x="822" y="505" width="46" height="34"/>
    <rect x="827" y="511" width="5" height="5"/><line x1="836" y1="513.5" x2="860" y2="513.5"/>
    <rect x="827" y="520" width="5" height="5"/><line x1="836" y1="522.5" x2="856" y2="522.5"/>
    <rect x="827" y="529" width="5" height="5"/><line x1="836" y1="531.5" x2="852" y2="531.5"/>
    <circle cx="872" cy="537" r="11" fill="#fff"/>
  </g>
  <path d="M866 537 l4 4 l9 -10" fill="none" stroke="var(--orange)" stroke-width="2.2"/>

  <!-- email icon -->
  <g fill="none" stroke="var(--navy)" stroke-width="1.6">
    <rect x="1063" y="515" width="36" height="25"/>
    <path d="M1063 515 L1081 530 L1099 515"/>
  </g>
  <circle cx="1081" cy="507" r="8" fill="#fff" stroke="var(--orange)" stroke-width="2"/>
  <circle cx="1081" cy="507" r="3" fill="none" stroke="var(--orange)" stroke-width="1.6"/>
  <g stroke="var(--orange)" stroke-width="2">
    <line x1="1104" y1="522" x2="1120" y2="522"/>
    <line x1="1104" y1="528" x2="1125" y2="528"/>
    <line x1="1104" y1="534" x2="1117" y2="534"/>
  </g>

  <!-- calendar icon -->
  <g fill="none" stroke="var(--navy)" stroke-width="1.6">
    <rect x="544" y="640" width="36" height="30"/>
    <line x1="544" y1="647" x2="580" y2="647"/>
    <line x1="551" y1="636" x2="551" y2="643"/><line x1="562" y1="636" x2="562" y2="643"/><line x1="573" y1="636" x2="573" y2="643"/>
    <rect x="549" y="652" width="5" height="4"/><rect x="557" y="652" width="5" height="4"/><rect x="565" y="652" width="5" height="4"/>
    <rect x="549" y="660" width="5" height="4"/><rect x="557" y="660" width="5" height="4"/>
  </g>
  <circle cx="582" cy="668" r="8" fill="#fff" stroke="var(--orange)" stroke-width="3" stroke-dasharray="3 2"/>
  <circle cx="582" cy="668" r="3" fill="var(--orange)"/>
</svg>

<div class="t brand">
  <span class="brand-row">
    <span class="brand-dot"></span>
    <span class="brand-text">
      <span class="brand-name">VELMARKPARTNERS</span>
      <span class="brand-tag">PERFORMANCE MARKETING</span>
    </span>
  </span>
</div>

<div class="t stage-title title-1">B2B LOOKALIKE <span class="accent">AUDIENCES</span></div>
<div class="t stage-title title-2">ABM TARGETING</div>

<div class="t partner p-orvanta">orvanta</div>
<div class="t partner p-pellucid">pellucid</div>
<div class="t partner p-keystat">Keystat Data</div>
<div class="t partner p-tidewell">Tidewell</div>
<div class="t partner p-marrowline">marrowline</div>

<div class="t step-label s-outreach">OUTREACH &amp; OFFER</div>
<div class="t step-label s-prequal">PRE-QUALIFICATION QUESTION</div>
<div class="t step-label s-email">EMAIL FOLLOW UP</div>
<div class="t step-label s-appoint">APPOINTMENT SETTING</div>
</body>
</html>
```